Bramble Peak Information Technology Business Card
Services for Move Add Change, Technical Relocation, Server Room Support, Technical Support
Bramble Peak Information Technology Business Card - Information Technology
Creative Brief
Professional
Owen Darlisk
2917 41st Lane Northeast Seattle WA 98422
owen@bramblepkit-example.com
www.bramblepkit-example.com
The original logo on the back, #34 and #35
Move Add and Changes, Corporate Relocation, Server Room Support, Technical Support

```html
<!DOCTYPE html>
<html lang="en">
<head>
<meta charset="utf-8">
<title>Bramble Peak Information Technology – Business Card</title>
<link href="https://fonts.googleapis.com/css2?family=Montserrat:wght@400;500;600;800&display=swap" rel="stylesheet">
<style>
  :root {
    --backdrop: #d9d6d1;
    --card-top: #f4f5f6;
    --card-bottom: #e3e5e8;
    --brand-ink: #3b3d40;
    --accent: #f39a1e;
    --band: #3a3b3e;
    --band-edge: #2c2d30;
    --band-text: #f2f2f2;
    --divider: #8a8b8e;
    --web-text: #55575b;
  }
  * { box-sizing: border-box; margin: 0; padding: 0; }
  html, body { width: 1200px; height: 770px; overflow: hidden; }
  body {
    background: var(--backdrop);
    display: flex; align-items: center; justify-content: center;
    font-family: "Montserrat", sans-serif;
  }
  .business-card {
    position: relative;
    width: 1000px; height: 660px;
    border-radius: 22px;
    background: linear-gradient(180deg, var(--card-top) 0%, var(--card-bottom) 100%);
    box-shadow: 0 18px 40px rgba(0,0,0,0.18);
    overflow: hidden;
  }
  .brand {
    position: absolute; top: 118px; left: 0; right: 0;
    display: flex; align-items: center; justify-content: center; gap: 22px;
  }
  .brand-dot { width: 44px; height: 44px; border-radius: 50%; background: var(--accent); }
  .brand-name {
    font-weight: 800; font-size: 66px; letter-spacing: 1px;
    color: var(--brand-ink); line-height: 1;
  }
  .info-band {
    position: absolute; left: 0; right: 0; top: 283px; height: 207px;
    background: linear-gradient(180deg, var(--band) 0%, var(--band-edge) 100%);
  }
  .band-notch {
    position: absolute; left: 222px; top: -22px;
    width: 0; height: 0;
    border-left: 22px solid transparent; border-right: 22px solid transparent;
    border-bottom: 22px solid var(--band);
  }
  .person { position: absolute; left: 100px; top: 68px; }
  .person-name {
    color: var(--accent); font-weight: 500; font-size: 30px; letter-spacing: 1px;
    text-transform: uppercase;
  }
  .person-title { color: var(--band-text); font-size: 23px; font-weight: 500; margin-top: 8px; padding-left: 44px; }
  .band-divider {
    position: absolute; left: 468px; top: 36px; bottom: 36px; width: 2px; background: var(--divider);
  }
  .contact-list { position: absolute; left: 510px; top: 44px; list-style: none; }
  .contact-list li {
    display: flex; align-items: center; gap: 16px;
    color: var(--band-text); font-size: 21px; height: 38px;
  }
  .contact-icon { width: 26px; height: 26px; flex: none; }
  .web-strip {
    position: absolute; left: 0; right: 0; top: 530px;
    display: flex; align-items: center; justify-content: center; gap: 18px;
  }
  .web-rule { width: 120px; height: 2px; background: var(--divider); opacity: .6; }
  .web-address { color: var(--web-text); font-size: 22px; font-weight: 600; letter-spacing: 2px; }
</style>
</head>
<body>
  <div class="business-card">
    <div class="brand">
      <span class="brand-dot"></span>
      <span class="brand-name">BRAMBLE PEAK</span>
    </div>

    <div class="info-band">
      <span class="band-notch"></span>
      <div class="person">
        <p class="person-name">Owen Darlisk</p>
        <p class="person-title">Managing Director</p>
      </div>
      <span class="band-divider"></span>
      <ul class="contact-list">
        <li>
          <svg class="contact-icon" viewBox="0 0 26 26"><circle cx="13" cy="13" r="13" fill="var(--accent)"/><path d="M9 7c1 0 2 2 2 3s-1 1-1 2 2 3 3 3 1-1 2-1 3 1 3 2-1 3-3 3c-4 0-8-5-8-9 0-2 1-3 2-3z" fill="var(--band)"/></svg>
          012 555 0147
        </li>
        <li>
          <svg class="contact-icon" viewBox="0 0 26 26"><circle cx="13" cy="13" r="13" fill="var(--accent)"/><path d="M9 7c1 0 2 2 2 3s-1 1-1 2 2 3 3 3 1-1 2-1 3 1 3 2-1 3-3 3c-4 0-8-5-8-9 0-2 1-3 2-3z" fill="var(--band)"/></svg>
          012 555 0148
        </li>
        <li>
          <svg class="contact-icon" viewBox="0 0 26 26"><circle cx="13" cy="13" r="13" fill="var(--accent)"/><rect x="6.5" y="8.5" width="13" height="9" rx="1" fill="var(--band)"/><path d="M7 9l6 5 6-5" fill="none" stroke="var(--accent)" stroke-width="1.3"/></svg>
          owen@bramblepkit-example.com
        </li>
        <li>
          <svg class="contact-icon" viewBox="0 0 26 26"><circle cx="13" cy="13" r="13" fill="var(--accent)"/><path d="M13 6a5 5 0 0 1 5 5c0 4-5 9-5 9s-5-5-5-9a5 5 0 0 1 5-5z" fill="var(--band)"/><circle cx="13" cy="11" r="1.8" fill="var(--accent)"/></svg>
          2917 41st Lane Northeast
        </li>
      </ul>
    </div>

    <div class="web-strip">
      <span class="web-rule"></span>
      <span class="web-address">www.bramblepkit-example.com</span>
      <span class="web-rule"></span>
    </div>
  </div>
</body>
</html>
```